Acai Label - 2oz

I'm going to need a graphic label for 2oz Torvik Glass bottle. My company is Velmora Brands and this particular product is an energy shot. (organic). Please see attachments for example.
Dimensions of Bottle - I need a full wrap concept
Color: Amber
Size: 2 oz
Material: Glass
Case Pack: 240
Neck finish: 20-400
Height: 3.687 in / 9.365 cm
Diameter: 1.52 in / 3.861 cm
Label Dimensions: 4.625 x 1.75 in
Print Dimensions: 4.75 x 1.75 in
Please incorporate existing Velmora Brands Logo on label.
Target Market(s)
Target market is - people that are interested natural forms of an energy boost.
Ages from 16- 40. I'd like it to appeal to broad spectrum of people. Please submit all creative designs and refinement can always come after.
Industry/Entity Type
It Company
Look and feel

```html
<!DOCTYPE html>
<html lang="en">
<head>
<meta charset="utf-8">
<title>Velmora Brands – Acai Organic Energy Shot Label</title>
<link rel="stylesheet" href="https://fonts.googleapis.com/css2?family=Arimo:wght@400;700&display=swap">
<style>
  :root {
    --stage: #0a0a0a;
    --label-white: #fbfbf9;
    --ink-navy: #1b1d3a;
    --brand-green: #4a9a2e;
    --ribbon-teal: #2f7d6c;
    --ribbon-teal-dark: #1f5a4d;
    --ribbon-text: #ffffff;
    --honeycomb-tint: #e3efdf;
    --berry-dark: #1c1a33;
    --berry-mid: #34315a;
    --pill-teal: #2f7d6c;
    --band-gold: #c99a12;
    --band-gold-light: #e8c547;
    --band-green: #28b23a;
    --band-green-light: #7ee08a;
    --band-teal: #1fb38a;
    --band-teal-light: #79e0c2;
  }
  * { box-sizing: border-box; margin: 0; padding: 0; }
  html, body {
    width: 1200px; height: 901px; overflow: hidden;
    background: var(--stage);
    font-family: "Arimo", Arial, sans-serif;
  }
  .label-set {
    position: absolute; left: 130px; top: 230px;
    display: flex; gap: 80px;
  }
  .label {
    position: relative; width: 260px; height: 440px;
    background: var(--label-white);
    overflow: hidden;
  }
  .label__band {
    position: absolute; left: 0; right: 0; height: 24px;
    background: linear-gradient(90deg, var(--band) 0%, var(--band-light) 50%, var(--band) 100%);
  }
  .label__band--top { top: 0; }
  .label__band--bottom { bottom: 0; }
  .label--gold  { --band: var(--band-gold);  --band-light: var(--band-gold-light); }
  .label--green { --band: var(--band-green); --band-light: var(--band-green-light); }
  .label--teal  { --band: var(--band-teal);  --band-light: var(--band-teal-light); }

  .label__brand {
    position: absolute; top: 62px; left: 0; right: 0;
    display: flex; justify-content: center; align-items: center; gap: 6px;
  }
  .label__brand-dot {
    width: 14px; height: 14px; border-radius: 50%;
    background: var(--brand-green);
  }
  .label__brand-name {
    font-size: 16px; font-weight: 700; color: var(--brand-green);
  }
  .label__product {
    position: absolute; top: 102px; left: 0; right: 0; text-align: center;
    font-size: 64px; font-weight: 700; color: var(--ink-navy); letter-spacing: -1px;
    line-height: 1.1;
  }
  .label__honeycomb {
    position: absolute; left: 0; right: 0; top: 205px; bottom: 24px;
    background: linear-gradient(180deg, var(--label-white) 0%, var(--honeycomb-tint) 35%, var(--honeycomb-tint) 100%);
  }
  .label__ribbon {
    position: absolute; top: 188px; left: 12px; width: 236px; height: 46px;
  }
  .label__ribbon-text {
    font-family: "Arimo", Arial, sans-serif; font-size: 15px; fill: var(--ribbon-text);
  }
  .label__fruit {
    position: absolute; top: 244px; left: 30px; width: 200px; height: 120px;
    border-radius: 14px;
    background: linear-gradient(180deg, var(--berry-mid) 0%, var(--berry-dark) 100%);
  }
  .label__size {
    position: absolute; top: 382px; left: 50%; transform: translateX(-50%);
    padding: 3px 14px; border-radius: 8px;
    background: var(--pill-teal); color: var(--ribbon-text);
    font-size: 13px; line-height: 1.2;
  }
</style>
</head>
<body>
  <main class="label-set">
    <section class="label label--gold" aria-label="Acai label, gold variant">
      <div class="label__band label__band--top"></div>
      <div class="label__honeycomb" role="img" aria-label="Pale green honeycomb pattern"></div>
      <div class="label__brand"><span class="label__brand-dot"></span><span class="label__brand-name">Velmora Brands</span></div>
      <h1 class="label__product">Acai</h1>
      <svg class="label__ribbon" viewBox="0 0 236 46">
        <polygon points="0,14 22,14 22,40 0,40 8,27" fill="var(--ribbon-teal-dark)"/>
        <polygon points="236,14 214,14 214,40 236,40 228,27" fill="var(--ribbon-teal-dark)"/>
        <path d="M16 6 Q118 -2 220 6 L220 34 Q118 26 16 34 Z" fill="var(--ribbon-teal)"/>
        <text class="label__ribbon-text" x="118" y="24" text-anchor="middle">organic Energy Shot</text>
      </svg>
      <div class="label__fruit" role="img" aria-label="Acai berry cluster with mint leaves illustration"></div>
      <div class="label__size">2 oz</div>
      <div class="label__band label__band--bottom"></div>
    </section>

    <section class="label label--green" aria-label="Acai label, green variant">
      <div class="label__band label__band--top"></div>
      <div class="label__honeycomb" role="img" aria-label="Pale green honeycomb pattern"></div>
      <div class="label__brand"><span class="label__brand-dot"></span><span class="label__brand-name">Velmora Brands</span></div>
      <h1 class="label__product">Acai</h1>
      <svg class="label__ribbon" viewBox="0 0 236 46">
        <polygon points="0,14 22,14 22,40 0,40 8,27" fill="var(--ribbon-teal-dark)"/>
        <polygon points="236,14 214,14 214,40 236,40 228,27" fill="var(--ribbon-teal-dark)"/>
        <path d="M16 6 Q118 -2 220 6 L220 34 Q118 26 16 34 Z" fill="var(--ribbon-teal)"/>
        <text class="label__ribbon-text" x="118" y="24" text-anchor="middle">organic Energy Shot</text>
      </svg>
      <div class="label__fruit" role="img" aria-label="Acai berry cluster with mint leaves illustration"></div>
      <div class="label__size">2 oz</div>
      <div class="label__band label__band--bottom"></div>
    </section>

    <section class="label label--teal" aria-label="Acai label, teal variant">
      <div class="label__band label__band--top"></div>
      <div class="label__honeycomb" role="img" aria-label="Pale green honeycomb pattern"></div>
      <div class="label__brand"><span class="label__brand-dot"></span><span class="label__brand-name">Velmora Brands</span></div>
      <h1 class="label__product">Acai</h1>
      <svg class="label__ribbon" viewBox="0 0 236 46">
        <polygon points="0,14 22,14 22,40 0,40 8,27" fill="var(--ribbon-teal-dark)"/>
        <polygon points="236,14 214,14 214,40 236,40 228,27" fill="var(--ribbon-teal-dark)"/>
        <path d="M16 6 Q118 -2 220 6 L220 34 Q118 26 16 34 Z" fill="var(--ribbon-teal)"/>
        <text class="label__ribbon-text" x="118" y="24" text-anchor="middle">organic Energy Shot</text>
      </svg>
      <div class="label__fruit" role="img" aria-label="Acai berry cluster with mint leaves illustration"></div>
      <div class="label__size">2 oz</div>
      <div class="label__band label__band--bottom"></div>
    </section>
  </main>
</body>
</html>
```